Fun/Happy Business Card & New Logo for Home Cake Shop

We need a business card for a small home-based, 2 person husband/wife bakery where we do cakes, cupcakes, eclairs, cream puffs and such. Our company name is Tiny Sunny Bakes.

We generally like the colour pink, but are open to other colour scheme ideas as well. The head chef(wife) is a very fun-loving, always cheerful and happy person and we want the business card to reflect her bubbly personality.

The business card should contain the husband's name AND the wife's name.
Updates

1st place prize money has been increased as requested. Thanks for your designs so far! 

Target Market(s)

Generally adults, for birthdays or small/medium sized catering events.

Industry/Entity Type

Bakery

Requirements
Must have
• Name 1: Marisol Tan
Phone: 93816257

Name 2: Koren Tan
Phone: 97421560

Email: info@tinysunnybakes.example
Website: www.tinysunnybakes.example

Additional Info, Edit: Please ensure that the logo contains a cake and at least a couple cupcakes.
Nice to have
• I have uploaded a couple images with the general feel of what we want. The logo should be one with a cake and some cupcakes around it, with the words Tiny Sunny Bakes. Try to come up with something more impressive than the current logo we have.

For the draft name card I uploaded in the file, that is also what we're sort of looking at. Try to come up with something more impressive/creative than that name card as well.

For the back of the name card, we are happy with just having the logo there. We're not sure what colour scheme would go best just yet, so feel free to show us your creative minds! :)

Additional Info, Edit: Please try to come up with a more realistic type of cake and cupcakes in the logo. We do not want it to be too cartoony. The attached images are just examples of the format.
Should not have
• Wordings or images that indicate 'Phone', 'Email' or 'Website' do not need to be included. Our customer base should be able to identify what an email and a website looks like. However, if you find that it looks particularly better, then feel free to be creative.

```html
<!DOCTYPE html>
<html lang="en">
<head>
<meta charset="utf-8">
<title>Tiny Sunny Bakes – Business Card</title>
<link rel="stylesheet" href="https://fonts.googleapis.com/css2?family=Comfortaa:wght@300;400&display=swap">
<style>
  :root {
    --paper: #ffffff;
    --berry: #e6217f;
    --violet: #9a2ee6;
    --blush: #f07ab8;
  }
  * { margin: 0; padding: 0; box-sizing: border-box; }
  html, body {
    width: 1200px;
    height: 900px;
    overflow: hidden;
    background: var(--paper);
  }
  .card {
    position: relative;
    width: 1200px;
    height: 900px;
    background: var(--paper);
    font-family: "Comfortaa", sans-serif;
    font-weight: 300;
  }
  .brand-mark {
    position: absolute;
    left: 450px;
    top: 40px;
    width: 300px;
    height: 300px;
    background: var(--blush);
    border-radius: 6px;
  }
  .brand-name {
    position: absolute;
    left: 0;
    top: 378px;
    width: 1200px;
    text-align: center;
    font-size: 62px;
    color: var(--berry);
    letter-spacing: 1px;
  }
  .owners {
    position: absolute;
    left: 20px;
    right: 18px;
    top: 548px;
    display: flex;
    justify-content: space-between;
    align-items: baseline;
    font-size: 74px;
    color: var(--violet);
    white-space: nowrap;
  }
  .owners .amp { color: var(--berry); font-size: 62px; }
  .phone {
    position: absolute;
    top: 648px;
    font-size: 42px;
    color: var(--berry);
    text-align: center;
    width: 360px;
  }
  .phone--koren { left: 90px; }
  .phone--marisol { left: 735px; }
  .email, .website {
    position: absolute;
    left: 0;
    width: 1200px;
    text-align: center;
  }
  .email { top: 755px; font-size: 34px; color: var(--violet); }
  .website { top: 818px; font-size: 38px; color: var(--berry); }
</style>
</head>
<body>
  <main class="card">
    <div class="brand-mark" aria-hidden="true"></div>
    <h1 class="brand-name">Tiny Sunny Bakes</h1>

    <p class="owners">
      <span class="owner">Koren Tan</span>
      <span class="amp">&amp;</span>
      <span class="owner">Marisol Tan</span>
    </p>
    <p class="phone phone--koren">97421560</p>
    <p class="phone phone--marisol">93816257</p>

    <p class="email">info@tinysunnybakes.example</p>
    <p class="website">www.tinysunnybakes.example</p>
  </main>
</body>
</html>
```